BrackenLeaf Billboards

We already hava a logo, slogan and general theme, we are looking for 2 to 3 billboard designs for out Recreational-Use Retail Cannabis Dispensary in NY state. We would like for the billboard to be a "Space" theme with a realistic-looking astronaut, we cannot have any "cartoon-like" images that would be attractive to children per state regulations. We would like the following wording included:
BrackenLeaf Cannabis Company - Oswego , slogan is "Products out of this world" , address of 287 Harlow Street - Oswego, Free Delivery - Orders over $150 . Our primary brand color is lime green.

```html
<!DOCTYPE html>
<html lang="en">
<head>
<meta charset="utf-8">
<title>BrackenLeaf Billboard</title>
<link rel="stylesheet" href="https://fonts.googleapis.com/css2?family=Poppins:wght@500;600&family=Roboto+Condensed:ital,wght@1,800;1,900&display=swap">
<style>
  :root {
    --page: #ececec;
    --ink: #050605;
    --lime: #7ed321;
    --lime-deep: #4f9a12;
    --white: #ffffff;
    --glow: rgba(88, 180, 40, 0.55);
    --violet: rgba(90, 40, 120, 0.5);
  }
  * { margin: 0; padding: 0; box-sizing: border-box; }
  html, body { width: 932px; height: 1200px; overflow: hidden; background: var(--page); }
  .canvas { position: relative; width: 932px; height: 1200px; }

  .billboard {
    position: absolute; left: 16px; top: 470px; width: 900px; height: 261px;
    background:
      radial-gradient(ellipse 260px 120px at 470px 150px, var(--glow), transparent 70%),
      radial-gradient(ellipse 180px 110px at 610px 235px, rgba(70,150,30,0.45), transparent 70%),
      radial-gradient(ellipse 120px 120px at 60px 70px, var(--violet), transparent 70%),
      radial-gradient(ellipse 90px 140px at 880px 150px, var(--violet), transparent 70%),
      var(--ink);
    box-shadow: 0 12px 18px rgba(0,0,0,0.35);
    overflow: hidden;
  }
  .backdrop-scene {
    position: absolute; left: 0; right: 0; bottom: 0; height: 110px;
    background: linear-gradient(180deg, transparent, rgba(30,70,20,0.55) 55%, rgba(5,8,5,0.9));
  }

  .brand {
    position: absolute; left: 26px; top: 30px; width: 210px;
    text-align: center; color: var(--white);
    font-family: 'Poppins', sans-serif; font-weight: 500; line-height: 1.15;
  }
  .brand-name { font-size: 22px; letter-spacing: 0.5px; }
  .brand-sub { font-size: 13px; letter-spacing: 0.8px; text-transform: uppercase; }
  .brand-rule { width: 160px; height: 1px; background: var(--white); margin: 3px auto 4px; }
  .brand-town { font-size: 13px; letter-spacing: 1.5px; text-transform: uppercase; }

  .headline {
    position: absolute; font-family: 'Roboto Condensed', sans-serif;
    font-style: italic; font-weight: 900; color: var(--white); line-height: 1;
    text-transform: uppercase; letter-spacing: -1px;
  }
  .headline-top { left: 250px; top: 28px; font-size: 68px; }
  .headline-main { left: 362px; top: 80px; font-size: 104px; letter-spacing: -3px; }
  .tag {
    position: absolute; left: 246px; top: 97px; width: 122px; height: 36px;
    background: var(--lime); border-radius: 3px;
    font-family: 'Roboto Condensed', sans-serif; font-style: italic; font-weight: 800;
    font-size: 25px; color: var(--ink); text-align: center; line-height: 36px;
  }

  .astronaut {
    position: absolute; left: 640px; top: 22px; width: 190px; height: 168px;
    background: radial-gradient(ellipse at 50% 45%, #e4e7e2 0%, #a9b3a4 45%, rgba(60,110,40,0.35) 75%, transparent 100%);
    border-radius: 40%;
  }

  .offer { position: absolute; left: 30px; top: 184px; height: 46px; display: flex; align-items: center; }
  .megaphone {
    width: 52px; height: 44px; margin-right: -6px; position: relative; z-index: 1;
    background: linear-gradient(135deg, #f2f2f2, #b8e07c 60%, var(--lime-deep));
    border-radius: 40% 10% 10% 40%;
  }
  .offer-free {
    background: var(--lime); height: 46px; width: 118px; padding-left: 16px;
    font-family: 'Roboto Condensed', sans-serif; font-style: italic; color: var(--ink);
    display: flex; flex-direction: column; justify-content: center; line-height: 0.9;
  }
  .offer-free strong { font-weight: 900; font-size: 31px; }
  .offer-free span { font-weight: 800; font-size: 11px; letter-spacing: 2.5px; }
  .offer-min {
    height: 46px; width: 100px; border: 1px solid var(--lime); border-left: none;
    background: var(--ink); color: var(--white); text-align: center;
    display: flex; flex-direction: column; justify-content: center;
    font-family: 'Roboto Condensed', sans-serif; font-style: italic;
  }
  .offer-min small { font-size: 7px; font-weight: 800; color: var(--lime); letter-spacing: 0.3px; }
  .offer-min b { font-size: 30px; font-weight: 900; line-height: 0.95; }
  .offer-min b sup { font-size: 14px; }

  .contact {
    position: absolute; top: 200px; display: flex; align-items: center; gap: 6px;
    font-family: 'Poppins', sans-serif; font-weight: 600; font-size: 21px; color: var(--white);
  }
  .contact-phone { left: 306px; }
  .contact-address { left: 522px; }
  .contact svg { width: 22px; height: 22px; flex: none; }
</style>
</head>
<body>
<main class="canvas">
  <section class="billboard">
    <div class="backdrop-scene" role="img" aria-label="Dark alien landscape with mountain silhouettes and green glow"></div>

    <div class="brand">
      <div class="brand-name">BrackenLeaf</div>
      <div class="brand-sub">Cannabis Company</div>
      <div class="brand-rule"></div>
      <div class="brand-town">Oswego</div>
    </div>

    <div class="headline headline-top">Products</div>
    <div class="headline headline-main">World</div>
    <div class="tag">Out of this</div>

    <div class="astronaut" role="img" aria-label="Realistic astronaut floating in space before a green-lit planet"></div>

    <div class="offer">
      <div class="megaphone" role="img" aria-label="Lime green megaphone"></div>
      <div class="offer-free"><strong>FREE</strong><span>DELIVERY</span></div>
      <div class="offer-min"><small>ORDERS OVER</small><b><sup>$</sup>150</b></div>
    </div>

    <div class="contact contact-phone">
      <svg viewBox="0 0 24 24" aria-hidden="true"><circle cx="12" cy="12" r="12" fill="var(--lime)"/><path d="M8.3 6.5l1.8-.4 1.1 2.8-1.3 1c.6 1.3 1.6 2.3 2.9 2.9l1-1.3 2.8 1.1-.4 1.8c-.2.6-.7 1-1.4 1-4.2-.3-7.5-3.6-7.8-7.8 0-.6.5-1.1 1.3-1.1z" fill="var(--ink)"/></svg>
      (315) 555-0147
    </div>
    <div class="contact contact-address">
      <svg viewBox="0 0 24 24" aria-hidden="true"><circle cx="12" cy="12" r="12" fill="var(--lime)"/><path d="M12 5a4.2 4.2 0 0 0-4.2 4.2c0 3.1 4.2 8 4.2 8s4.2-4.9 4.2-8A4.2 4.2 0 0 0 12 5zm0 5.8a1.6 1.6 0 1 1 0-3.2 1.6 1.6 0 0 1 0 3.2z" fill="var(--ink)"/></svg>
      287 Harlow Street - Oswego
    </div>
  </section>
</main>
</body>
</html>
```